Just Listed and Just Sold Post Cards. I have attached copies of what I have had in the past for reference. I have a new company logo attached that needs to be used. Please also include website: www.fernharborfinder.com
email. martawilkes@martawilkeshomes.com
phone 941-555-0173
Target Market(s)
home and land owners
Font styles to use
Sans Serif
Colors
0356a4
Requirements
Must have
- I need a South Gulf Cove Just Listed Card and a Just Sold Card
- Must have My name company name logo website email phone number
- back should read _______. on your block of South Gulf Cove has just SOLD at $________ on _____________________ similar to the one I have attached.
Nice to have
- I like how the attached postcards from before have the shaded picture on the back of the picture on the front. I like to have the aerial as one main photo and the photo with the boat as the other main photo.
- Integrate my Marta Wilkes logo with the TK Meridian logo

```html
<!DOCTYPE html>
<html lang="en">
<head>
<meta charset="utf-8">
<title>South Gulf Cove Just Listed Postcard</title>
<link rel="stylesheet" href="https://fonts.googleapis.com/css2?family=Cinzel:wght@500;600&family=Crimson+Pro:wght@400;500&family=Source+Sans+3:wght@400;600;700&display=swap">
<style>
  :root {
    --brand: #0356a4;
    --navy: #0b2a6e;
    --ink-blue: #1e4c9a;
    --stripe: #0d4fb0;
    --paper: #ffffff;
    --grey-text: #5a6170;
    --rule: #b9bec6;
    --stage: #eef0f3;
  }
  * { box-sizing: border-box; margin: 0; padding: 0; }
  html, body { width: 792px; height: 1200px; overflow: hidden; background: var(--stage); }
  .sheet { position: relative; width: 792px; height: 1200px; }
  .postcard {
    position: absolute; left: 46px; width: 700px; height: 543px;
    background: var(--paper); overflow: hidden;
    box-shadow: 0 3px 10px rgba(0,0,0,.18);
    font-family: "Source Sans 3", sans-serif;
  }
  .postcard--front { top: 38px; }
  .postcard--back { top: 619px; }
  .postcard svg.art { position: absolute; inset: 0; }
  .abs { position: absolute; }

  /* front */
  .front-place { left: 28px; top: 22px; font-family: "Crimson Pro", serif; font-size: 25px; color: var(--ink-blue); }
  .front-headline { left: 24px; top: 58px; font-family: "Crimson Pro", serif; font-weight: 500; font-size: 68px; letter-spacing: 1px; color: #fff; line-height: 1; text-shadow: 0 2px 4px rgba(0,0,0,.25); }
  .brokerage-name { right: 30px; top: 44px; display: flex; align-items: center; gap: 8px; font-weight: 600; font-size: 21px; letter-spacing: 1.5px; color: var(--grey-text); text-transform: uppercase; }
  .brokerage-name .mark { width: 14px; height: 14px; border-radius: 50%; background: var(--grey-text); }
  .agent { color: #fff; text-align: center; }
  .agent-name { font-family: "Cinzel", serif; font-weight: 600; letter-spacing: 1.5px; line-height: 1; }
  .agent-title { font-family: "Cinzel", serif; font-weight: 500; letter-spacing: 2px; }
  .front-agent { left: 30px; top: 478px; }
  .front-agent .agent-name { font-size: 29px; }
  .front-agent .agent-title { font-size: 13px; margin-top: 3px; }
  .contact-list { right: 24px; top: 474px; list-style: none; color: #fff; font-size: 14.5px; text-align: right; line-height: 19px; }
  .contact-list li { display: flex; justify-content: flex-end; align-items: center; gap: 6px; }
  .contact-list .dot { width: 11px; height: 11px; border-radius: 50%; background: #5aa0e6; border: 1px solid #fff; }

  /* back */
  .back-agent { left: 40px; top: 70px; width: 330px; }
  .back-agent .agent-name { font-size: 32px; }
  .back-agent .agent-title { font-size: 14px; margin-top: 4px; }
  .fill-line { position: absolute; border-bottom: 1px solid #555; height: 0; }
  .form-text { font-size: 15px; color: #222; }
  .form-block { left: 12px; top: 215px; width: 355px; text-align: center; }
  .form-at { left: 18px; top: 272px; }
  .form-on { left: 192px; top: 272px; }
  .invite { left: 20px; top: 368px; width: 345px; text-align: center; color: #fff; font-size: 17.5px; line-height: 24px; text-shadow: 0 1px 3px rgba(0,0,0,.4); }
  .phone-pill { left: 60px; top: 439px; width: 257px; height: 32px; border-radius: 16px; background: #fff; display: flex; align-items: center; justify-content: center; gap: 8px; color: var(--brand); font-weight: 700; font-size: 22px; letter-spacing: 1px; }
  .back-web { left: 20px; top: 488px; width: 345px; text-align: center; color: #fff; font-weight: 700; font-size: 13.5px; letter-spacing: .5px; line-height: 19px; }
  .return-address { left: 405px; top: 27px; font-size: 12.5px; line-height: 14px; color: var(--grey-text); font-style: normal; }
  .stamp-box { left: 572px; top: 24px; width: 107px; height: 74px; border: 1px solid #aab; }
  .address-line { position: absolute; left: 415px; width: 264px; border-top: 1px solid var(--rule); }
</style>
</head>
<body>
<main class="sheet">

  <section class="postcard postcard--front" aria-label="Postcard front">
    <svg class="art" width="700" height="543" viewBox="0 0 700 543">
      <defs>
        <linearGradient id="aerialTone" x1="0" y1="0" x2="0" y2="1">
          <stop offset="0" stop-color="#2f63b0"/>
          <stop offset=".32" stop-color="#6a8fc4"/>
          <stop offset=".5" stop-color="#6f8795"/>
          <stop offset=".75" stop-color="#5f7467"/>
          <stop offset="1" stop-color="#4f6a45"/>
        </linearGradient>
        <linearGradient id="canalTone" x1="0" y1="0" x2="0" y2="1">
          <stop offset="0" stop-color="#c9d5e6"/>
          <stop offset=".35" stop-color="#7f9a8a"/>
          <stop offset=".55" stop-color="#6f8aa8"/>
          <stop offset="1" stop-color="#3f5f89"/>
        </linearGradient>
        <linearGradient id="fadeWhite" x1="0" y1="0" x2="0" y2="1">
          <stop offset="0" stop-color="#fff"/>
          <stop offset=".5" stop-color="#fff" stop-opacity=".85"/>
          <stop offset="1" stop-color="#fff" stop-opacity="0"/>
        </linearGradient>
        <linearGradient id="navyBand" x1="0" y1="0" x2="1" y2="0">
          <stop offset="0" stop-color="#0c3483"/>
          <stop offset="1" stop-color="#0a2a6c"/>
        </linearGradient>
      </defs>
      <rect role="img" aria-label="Aerial photo of South Gulf Cove canals and the gulf" x="0" y="0" width="700" height="470" fill="url(#aerialTone)"/>
      <path role="img" aria-label="Photo of a fishing boat on a canal in front of waterfront homes" d="M492,0 C470,130 445,290 430,470 L700,470 L700,0 Z" fill="url(#canalTone)"/>
      <rect x="470" y="0" width="230" height="120" fill="url(#fadeWhite)"/>
      <path d="M492,0 C470,130 445,290 430,470" fill="none" stroke="#fff" stroke-width="6"/>
      <path d="M0,390 C110,452 260,472 420,450 L560,438 C610,426 660,430 700,452 L700,543 L0,543 Z" fill="#fff"/>
      <path d="M0,402 C110,462 260,482 420,462 L560,448 C610,437 660,440 700,462 L700,543 L0,543 Z" fill="url(#navyBand)"/>
      <circle cx="413" cy="397" r="67" fill="#fff"/>
      <circle cx="413" cy="397" r="63" fill="var(--brand)"/>
      <circle role="img" aria-label="Map of Florida marking South Gulf Cove" cx="413" cy="397" r="58" fill="#dfe9dc"/>
    </svg>

    <p class="abs front-place">South Gulf Cove</p>
    <h1 class="abs front-headline">JUST LISTED</h1>
    <div class="abs brokerage-name"><span class="mark"></span>TK Meridian</div>

    <div class="abs agent front-agent">
      <div class="agent-name">MARTA WILKES</div>
      <div class="agent-title">BROKER ASSOCIATE</div>
    </div>
    <ul class="abs contact-list">
      <li>941-555-0173 <span class="dot"></span></li>
      <li>martawilkes@martawilkeshomes.com <span class="dot"></span></li>
      <li>www.fernharborfinder.com <span class="dot"></span></li>
    </ul>
  </section>

  <section class="postcard postcard--back" aria-label="Postcard back">
    <svg class="art" width="700" height="543" viewBox="0 0 700 543">
      <defs>
        <clipPath id="panelClip">
          <path d="M0,0 H326 C395,140 405,330 345,543 H0 Z"/>
        </clipPath>
        <linearGradient id="topPanel" x1="0" y1="0" x2="0" y2="1">
          <stop offset="0" stop-color="#1b4fa8"/>
          <stop offset="1" stop-color="#5b86c4"/>
        </linearGradient>
        <linearGradient id="shadedAerial" x1="0" y1="0" x2="0" y2="1">
          <stop offset="0" stop-color="#2d4f86"/>
          <stop offset=".5" stop-color="#2a4677"/>
          <stop offset="1" stop-color="#1a3468"/>
        </linearGradient>
      </defs>
      <g clip-path="url(#panelClip)">
        <rect x="0" y="0" width="420" height="152" fill="url(#topPanel)"/>
        <rect x="0" y="152" width="420" height="192" fill="#fff"/>
        <rect role="img" aria-label="Shaded aerial photo of South Gulf Cove" x="0" y="344" width="420" height="199" fill="url(#shadedAerial)"/>
      </g>
      <path d="M326,0 C395,140 405,330 345,543" fill="none" stroke="var(--stripe)" stroke-width="9"/>
      <path d="M338,0 C408,140 418,330 358,543" fill="none" stroke="#8fb0dc" stroke-width="1"/>
    </svg>

    <div class="abs agent back-agent">
      <div class="agent-name">MARTA WILKES</div>
      <div class="agent-title">BROKER ASSOCIATE</div>
    </div>

    <span class="fill-line" style="left:12px;top:208px;width:355px"></span>
    <p class="abs form-text form-block">on your block of South Gulf Cove has just LISTED</p>
    <p class="abs form-text form-at">at $</p>
    <span class="fill-line" style="left:47px;top:288px;width:130px"></span>
    <p class="abs form-text form-on">on</p>
    <span class="fill-line" style="left:222px;top:288px;width:145px"></span>

    <p class="abs invite">Please contact me if you are interested in buying or selling property in the area.</p>
    <div class="abs phone-pill">
      <svg width="20" height="20" viewBox="0 0 20 20" aria-hidden="true"><circle cx="10" cy="10" r="8.5" fill="none" stroke="currentColor" stroke-width="1.8"/><path d="M7.2,5.5 L8.6,7.8 L7.7,8.8 C8.3,10 9.6,11.4 11,12 L12,11.1 L14.3,12.5 L13.4,14.1 C10,13.8 6.6,10.3 6,7 Z" fill="currentColor"/></svg>
      941-555-0173
    </div>
    <p class="abs back-web">martawilkes@martawilkeshomes.com<br>www.fernharborfinder.com</p>

    <address class="abs return-address">Marta Wilkes<br>Thornton Kale Realty<br>312 W. 6th St.<br>PO Box 418<br>Palm Cove, FL 33990</address>
    <div class="abs stamp-box"></div>
    <span class="address-line" style="top:214px"></span>
    <span class="address-line" style="top:258px"></span>
    <span class="address-line" style="top:302px"></span>
    <span class="address-line" style="top:347px"></span>
  </section>

</main>
</body>
</html>
```